A5 2 sided flyer to promote pharmacy services

We need a leaflet design which promotes our pharmacy and its services. We are a modern, chic hip, funky new pharmacy, and our leaflet should reflect this.
We are looking for an exciting design fun design with limited pictures of people on it.
It needs to be 2 sided, the first side to include name, address, telephone number, twitter and facebook handle, opening hours. I want to highlight our main service with is prescription collection, I like the idea of having a cartoon type image: cartoon 1- ordering prescription, cartoon 2- dispensing medication, cartoon 3- patient collecting prescritpion.
I also need to highlight our services which include
medicine use review
pharmacy first*
Morning after pill*
emergency supply service*
seasonal flu vaccinations*
on the other side i need a consent form for ETP nomination to include full name, address, date of birth, NHS number, signature and current date
this shoudl be on the top half of the leaftet.
On the bottom half or bottom quarter, I need writing:
Thornfield Pharmacy proudly uses a robotic dispensing system.

The Pharmacy directors have invested in this technology to enhance the service that we provide our customers.

Medication is dispensed from a high speed robotic arm within the unit which not only improves efficiency but also importantly maximises patient safety.

The robot in action can be witnessed through a viewing window positioned outside the shop window - it is truly remarkable to see. Please feel free to visit and view. Our staff will be only too happy to introduce you to our new addition and explain how the system works.

Target Market(s)

NHS patients ranging from 16 years to 80 years +

Industry/Entity Type

Pharmacy

Font styles to use
Serif

Requirements
Must have
• Name of pharmacy
• Address of pharmacy: Ashcombe Larkfield Centre, Kestrel Row, Ashcombe, Nottingham, NG4 2TW
• Telephone number:0115 9630587
• Opening times: Mon - Sat 7.30am - 10pm, sunday 8am - 9pm
• Services we offer: Prescription collection service
• minor ailments scheme
• emergency hormonal contraception
• Expert health advice
• Medicines disposal
• Prescription delivery service
• Our twitter handle: ourthornfield
• facebook page: ourthornfieldpharmacy
Nice to have
• colourful, upbeat vibe to the leaflet whilst including all the relevant information.
Should not have
• big pictures of people

```html
<!DOCTYPE html>
<html lang="en">
<head>
<meta charset="utf-8">
<title>Thornfield Pharmacy – Flyer</title>
<link rel="stylesheet" href="https://fonts.googleapis.com/css2?family=Federo&family=Marcellus&display=swap">
<style>
  :root {
    --navy: #27288a;
    --navy-deep: #1f2078;
    --sky: #2a9fdc;
    --sky-light: #5cc3ee;
    --bullet-fade: #8c8fd0;
    --paper: #ffffff;
    --paper-shade: #eef0f4;
    --backdrop: #d9dadc;
  }
  * { box-sizing: border-box; margin: 0; padding: 0; }
  html, body { width: 1200px; height: 800px; overflow: hidden; }
  body {
    background: var(--backdrop);
    font-family: "Marcellus", Georgia, serif;
    color: var(--navy);
    position: relative;
  }
  .flyer {
    position: absolute;
    left: 320px; top: 4px;
    width: 560px; height: 792px;
    background: linear-gradient(180deg, var(--paper) 55%, var(--paper-shade) 100%);
    overflow: hidden;
    box-shadow: 0 6px 18px rgba(0,0,0,.18);
  }
  .hero {
    position: absolute; left: 0; top: 0;
    width: 560px; height: 370px;
    background:
      radial-gradient(ellipse 120px 70px at 75% 55%, rgba(240,100,42,.85), transparent 70%),
      radial-gradient(ellipse 90px 45px at 40% 40%, rgba(240,100,42,.55), transparent 70%),
      radial-gradient(ellipse 200px 60px at 60% 15%, rgba(240,100,42,.35), transparent 75%),
      linear-gradient(180deg, #f3efec 0%, #eef0f4 70%, #e8ebf1 100%);
  }
  .tagline {
    position: absolute; left: 42px; top: 232px;
    font-family: "Federo", "Marcellus", serif;
    font-size: 30px; line-height: 36px;
    color: var(--navy);
  }
  .band { position: absolute; left: 0; top: 370px; width: 560px; height: 16px; }
  .services { position: absolute; left: 222px; top: 430px; }
  .services h2 {
    font-weight: 400; font-size: 16px; letter-spacing: .3px;
    text-transform: uppercase; margin-bottom: 2px;
  }
  .services ul { list-style: none; }
  .services li {
    font-size: 15.5px; line-height: 21px; white-space: nowrap;
    display: flex; align-items: center; gap: 8px;
  }
  .services li::before {
    content: ""; width: 9px; height: 9px; background: var(--bullet); flex: none;
  }
  .contact {
    position: absolute; left: 222px; top: 594px;
    font-size: 13px; line-height: 17px; font-style: normal; white-space: nowrap;
  }
  .social {
    position: absolute; left: 222px; top: 662px;
    display: flex; gap: 16px; font-size: 13px; white-space: nowrap;
  }
  .social span { display: flex; align-items: center; gap: 8px; }
  .social i { width: 22px; height: 22px; background: var(--navy); display: block; }
  .social span.tw i { background: var(--sky); border-radius: 50%; }
  .brand { position: absolute; left: 14px; top: 520px; width: 200px; text-align: center; }
  .brand-mark {
    width: 90px; height: 90px; border-radius: 50%;
    background: var(--sky); margin: 0 auto 14px;
  }
  .brand-name { font-size: 34px; line-height: 36px; color: var(--navy); }
  .hours { position: absolute; left: 0; bottom: 0; width: 560px; height: 56px; }
  .hours p {
    position: absolute; left: 178px; top: 20px;
    font-size: 12px; letter-spacing: -.1px; color: #fff; white-space: nowrap;
  }
</style>
</head>
<body>
  <article class="flyer">
    <div class="hero" role="img" aria-label="Close-up photograph of orange and white medicine capsules scattered on a white surface"></div>
    <p class="tagline">Your Tagline<br>Goes Here</p>

    <svg class="band" viewBox="0 0 560 16" aria-hidden="true">
      <rect x="0" y="0" width="560" height="16" fill="var(--navy)"/>
      <polygon points="0,0 170,0 163,16 0,16" fill="var(--sky)"/>
      <rect x="0" y="0" width="92" height="16" fill="var(--sky-light)" opacity=".5"/>
    </svg>

    <section class="services">
      <h2>Services We Offer</h2>
      <ul>
        <li style="--bullet: var(--navy)">Prescription collection service</li>
        <li style="--bullet: #3235a0">Minor ailments scheme</li>
        <li style="--bullet: #4b4eb0">Emergency hormonal contraception</li>
        <li style="--bullet: #6366bd">Expert health advice</li>
        <li style="--bullet: #787bc7">Medicines disposal</li>
        <li style="--bullet: var(--bullet-fade)">Prescription delivery service</li>
      </ul>
    </section>

    <address class="contact">
      Ashcombe Larkfield Centre, Kestrel Row,<br>
      Ashcombe, Nottingham, NG4 2TW<br>
      Phone 0115 9630587
    </address>

    <div class="social">
      <span class="fb"><i></i>ourthornfieldpharmacy</span>
      <span class="tw"><i></i>ourthornfield</span>
    </div>

    <div class="brand">
      <div class="brand-mark"></div>
      <div class="brand-name">Thornfield<br>Pharmacy</div>
    </div>

    <footer class="hours">
      <svg width="560" height="56" viewBox="0 0 560 56" aria-hidden="true" style="position:absolute;left:0;top:0">
        <polygon points="152,0 560,0 560,56 168,56" fill="var(--navy-deep)"/>
      </svg>
      <p>Opening times: Mon - Sat 7.30am - 10pm, sunday 8am - 9pm</p>
    </footer>
  </article>
</body>
</html>
```